Plakat-Design für Immobilienmakler und Baufinanzierer
Zielgruppe
Wir sind Immobilienmakler und Baufinanzierer und suchen ein hochwertiges Design, unsere Zielgruppe sind Kunden, die Ihr Haus verkaufen möchten. Für jeden erfolgreichen Verkauf spenden wir 5 % unserer Maklercourtage an einen Verein, den sich der Kunde aussuchen darf. Mit diesem Plakat wollen wir auf unsere Vereinsförderng aufmerksam machen und Vereine ansprechen.
Aufgabenstellung
Text: 'Wir spenden 5 % unserer Provision für Ihren Verein', 'Nur 1,99 % Maklercourtage', Logo, Kontaktdaten

```html
<!DOCTYPE html>
<html lang="de">
<head>
<meta charset="utf-8">
<title>Plakat Vereinsförderung – Lindgart Immobilien</title>
<link rel="stylesheet" href="https://fonts.googleapis.com/css2?family=Raleway:wght@400;600;700;800&display=swap">
<style>
  :root {
    --backdrop: #d9d7d3;
    --paper: #efede9;
    --teal: #2a6b74;
    --stone: #9b928c;
    --white: #ffffff;
  }
  * { margin: 0; padding: 0; box-sizing: border-box; }
  html, body {
    width: 1200px; height: 1200px; overflow: hidden;
    background: var(--backdrop);
    font-family: "Raleway", sans-serif;
  }
  .poster {
    position: absolute; left: 192px; top: 30px;
    width: 815px; height: 1140px;
    background: var(--paper);
    overflow: hidden;
  }
  .brand {
    position: absolute; right: 48px; top: 82px;
    display: flex; align-items: center; gap: 10px;
    font-size: 24px; font-weight: 700; letter-spacing: 1.5px;
    color: var(--teal); text-transform: uppercase;
  }
  .brand-square { width: 14px; height: 14px; background: var(--teal); }
  .headline {
    position: absolute; left: 50px; top: 236px;
    font-weight: 800; font-size: 70px; line-height: 81px;
    text-transform: uppercase; letter-spacing: 0.5px;
  }
  .headline .teal { color: var(--teal); display: block; }
  .headline .stone { color: var(--stone); display: block; }
  .fee-tag {
    position: absolute; left: 50px; top: 565px;
    width: 425px; height: 61px;
    background: var(--stone); color: var(--white);
    font-weight: 700; font-size: 22px;
    display: flex; align-items: center; padding-left: 28px;
  }
  .footer-band {
    position: absolute; left: 0; bottom: 0;
    width: 100%; height: 144px; background: var(--teal);
  }
  .accent-band {
    position: absolute; left: 124px; top: 996px;
    width: 691px; height: 26px; background: var(--stone);
  }
  .contact {
    position: absolute; top: 1060px;
    color: var(--white); font-size: 15px; line-height: 19px;
  }
  .contact strong { font-weight: 700; }
  .contact-address { left: 115px; }
  .contact-phone { left: 332px; top: 1079px; }
  .contact-web { right: 37px; top: 1079px; }
</style>
</head>
<body>
  <main class="poster">
    <div class="brand"><span class="brand-square"></span>Lindgart Immobilien</div>

    <h1 class="headline">
      <span class="teal">Wir spenden 5&nbsp;%</span>
      <span class="stone">unserer Provision</span>
      <span class="teal">für Ihren Verein</span>
    </h1>

    <div class="fee-tag">NUR 1,99 % MAKLERCOURTAGE</div>

    <div class="footer-band"></div>
    <div class="accent-band"></div>

    <address class="contact contact-address" style="font-style:normal">
      <strong>Lindgart Immobilien</strong><br>
      Birkenallee 7<br>
      47800 Ahrenfeld
    </address>
    <div class="contact contact-phone">
      Tel: 02131 508 27 16<br>
      Mobil: 0171 624 085 39
    </div>
    <div class="contact contact-web">
      info@lindgart-immobilien.de<br>
      www.lindgart-immobilien.de
    </div>
  </main>
</body>
</html>
```